Business Card - MosswickTreasury.com

I need a business card that has my photo. It should say: My Pemakino store can be found on at the MosswickTreasury.com. Also find my links to Friendsly, Vidstream and Clipdance. (If this can be done graphically, then that's even better)

```html
<!DOCTYPE html>
<html lang="en">
<head>
<meta charset="utf-8">
<title>MosswickTreasury.com – Business Card</title>
<link rel="stylesheet" href="https://fonts.googleapis.com/css2?family=Josefin+Sans:wght@300;400;600&display=swap">
<style>
  :root {
    --stage: #2a2a2a;
    --card-white: #ffffff;
    --frame-grey: #8f8c88;
    --url-grey: #6e6b68;
    --card-black: #050505;
    --text-white: #f4f4f4;
    --social-blue: #3b5aa8;
    --social-red: #e0463a;
    --social-dark: #111111;
    --photo-light: #efece6;
    --photo-warm: #e3b53a;
  }
  * { box-sizing: border-box; margin: 0; padding: 0; }
  html, body { width: 1200px; height: 873px; overflow: hidden; }
  body {
    background: var(--stage);
    font-family: "Josefin Sans", sans-serif;
    position: relative;
  }
  .card {
    position: absolute;
    width: 640px;
    height: 366px;
    left: 280px;
  }
  .card-back {
    top: 50px;
    background: var(--frame-grey);
    padding: 22px;
  }
  .card-back__panel {
    width: 100%;
    height: 100%;
    background: var(--card-white);
    display: flex;
    align-items: center;
    justify-content: center;
  }
  .card-back__url {
    font-weight: 300;
    font-size: 27px;
    letter-spacing: 1px;
    color: var(--url-grey);
  }
  .card-front {
    top: 457px;
    display: flex;
    background: var(--card-black);
  }
  .card-front__info {
    width: 56%;
    color: var(--text-white);
    text-align: center;
    display: flex;
    flex-direction: column;
    align-items: center;
    justify-content: center;
    padding: 0 18px;
  }
  .store-intro { font-size: 15px; font-weight: 400; letter-spacing: 1px; }
  .store-url {
    font-size: 22px; font-weight: 600; letter-spacing: 2px; margin-top: 8px;
  }
  .divider { width: 28px; height: 2px; background: var(--text-white); margin: 12px 0; }
  .links-intro { font-size: 15px; letter-spacing: 1px; }
  .social-dots { display: flex; gap: 12px; margin-top: 10px; }
  .social-dot { width: 26px; height: 26px; border-radius: 50%; }
  .social-dot--friendsly { background: var(--social-blue); }
  .social-dot--vidstream { background: var(--social-red); }
  .social-dot--clipdance { background: var(--social-dark); border: 2px solid var(--text-white); }
  .social-names {
    display: flex; gap: 12px; margin-top: 14px; font-size: 16px; letter-spacing: 1px;
  }
  .social-name--friendsly { color: var(--social-blue); }
  .social-name--vidstream { color: var(--social-red); }
  .social-name--clipdance { color: var(--text-white); }
  .social-sep { color: var(--social-blue); }
  .card-front__photo {
    width: 44%;
    background: linear-gradient(180deg, var(--photo-light) 0%, var(--photo-light) 55%, var(--photo-warm) 78%, var(--photo-warm) 100%);
  }
</style>
</head>
<body>
  <section class="card card-back">
    <div class="card-back__panel">
      <p class="card-back__url">www.MosswickTreasury.com</p>
    </div>
  </section>

  <section class="card card-front">
    <div class="card-front__info">
      <p class="store-intro">My Pemakino store can be found on at the</p>
      <p class="store-url">www.MosswickTreasury.com</p>
      <span class="divider"></span>
      <p class="links-intro">Also find my links to</p>
      <div class="social-dots">
        <span class="social-dot social-dot--friendsly"></span>
        <span class="social-dot social-dot--vidstream"></span>
        <span class="social-dot social-dot--clipdance"></span>
      </div>
      <p class="social-names">
        <span class="social-name--friendsly">Friendsly</span>
        <span class="social-sep">|</span>
        <span class="social-name--vidstream">Vidstream</span>
        <span class="social-sep">|</span>
        <span class="social-name--clipdance">Clipdance</span>
      </p>
    </div>
    <div class="card-front__photo" role="img" aria-label="Portrait photo of the store owner wearing a yellow floral top"></div>
  </section>
</body>
</html>
```